Running Book Cover Design Project

My client has written a book about running and his accomplishments throughout the sport, his story etc. We need to get a cover designed for it. The book will be offered online only, but may later on look at printing a few copies later down the track, so it will need to be a vector graphic so we can resize it easily.

The title of the book is 'Beyond The Far Hill', written by Marco Tevin Alcaraza from the Philippines.

The idea that we have had for the cover is as follows... We would like the word 'step' so be somehow presented in a step, maybe we could use the shoe tread somehow with the word step in it, or use a step in some way, I will leave it up to you, we are pretty open.

Just think that finding running has changed his life and he wants that represented on the cover somehow with the title standing for both taking one more step with running and a metaphor for life.

Do note that the illustration of the 'foot step' has to be a mid-foot or forefoot landing on the ground instead of a heel strike. Reason being that heel strikes can lead to a lot of injuries; the author is against it as well.

UPDATE: The design should have the runner in summer clothes, with bold fonts, not running up steps as these are marathon type events he is running (attached a new image for inspiration), he should be wearing shoes and clothing similar to the attached images from Talvex
Updates

Changes:

AUTHOR - Colin Barr

Sorry about the inclusion of Marco, the author's name should be represented as Colin Barr

Still waiting on final approval, apologies!

Target Market(s)

Adults based in south east asia predominantly singapore and the philippines.

Targeted to all those who enjoy inspirational stories or books about running

Industry/Entity Type

Printing

Requirements
Must have
• Running imagery
Shoe/Step IIllustration
Title of Book
Author's Name

```html
<!DOCTYPE html>
<html lang="en">
<head>
<meta charset="utf-8">
<title>Beyond The Far Hill – Book Cover</title>
<link rel="stylesheet" href="https://fonts.googleapis.com/css2?family=Archivo+Black&family=Arimo:wght@400;700&family=Tinos:ital,wght@0,400;0,700;1,400&display=swap">
<style>
  :root {
    --lime: #6ed61c;
    --lime-spine: #62cc24;
    --title-green: #5fbf22;
    --title-light: #9bd43a;
    --text-green: #55bf2a;
    --ink: #111111;
    --paper: #ffffff;
    --frame: #8a9196;
    --step-ink: #1e1e1e;
  }
  * { margin: 0; padding: 0; box-sizing: border-box; }
  html, body { width: 1200px; height: 667px; overflow: hidden; background: var(--paper); }
  .canvas {
    position: relative; width: 1200px; height: 667px;
    border: 1px solid var(--frame); background: var(--paper);
  }
  .jacket {
    position: absolute; left: 43px; top: 68px; width: 1135px; height: 498px;
    border: 1px solid var(--frame); overflow: hidden;
  }
  .panel { position: absolute; top: 0; height: 100%; overflow: hidden; }

  /* Author flap */
  .flap-author { left: 0; width: 190px; background: var(--lime); color: var(--paper); padding: 26px 12px 0 18px; }
  .flap-author .deco {
    position: absolute; border-radius: 50%; border: 22px solid rgba(255,255,255,0.18);
  }
  .flap-author h2 { font: 700 17px/1 "Arimo", sans-serif; text-align: center; margin-bottom: 8px; position: relative; }
  .bio { font: 400 13px/15.2px "Tinos", serif; text-align: justify; position: relative; }
  .bio + .bio { margin-top: 12px; }
  .dropcap { float: left; font: 400 50px/40px "Tinos", serif; margin: 2px 3px 0 0; }

  /* Back cover */
  .back { left: 190px; width: 340px; }
  .back-photo {
    position: absolute; inset: 0;
    background: linear-gradient(180deg, #ffffff 0%, #ffffff 52%, #dfe3e0 62%, #b9bdbb 74%, #a3a8a5 88%, #b8bbb9 100%);
  }
  .back-photo::after {
    content: ""; position: absolute; left: 0; top: 210px; width: 160px; height: 150px;
    background: radial-gradient(ellipse at 30% 60%, rgba(120,140,110,0.55), rgba(255,255,255,0) 70%);
  }
  .back-head { position: absolute; left: 20px; top: 27px; width: 310px; font: 700 17px/24px "Arimo", sans-serif; color: var(--text-green); }
  .back-sub { position: absolute; right: 16px; top: 80px; font: 700 17px/1 "Arimo", sans-serif; color: var(--ink); }
  .back-copy { position: absolute; left: 20px; top: 117px; width: 306px; font: 400 13px/15px "Tinos", serif; color: var(--text-green); text-align: justify; }
  .back-copy p + p { margin-top: 15px; }
  .year { position: absolute; left: 160px; top: 461px; font: 700 15px/1 "Arimo", sans-serif; color: var(--ink); }

  /* Spine */
  .spine { left: 530px; width: 42px; background: var(--lime-spine); color: var(--paper); }
  .spine-title, .spine-author {
    position: absolute; left: 50%; writing-mode: vertical-rl; transform: translateX(-50%);
    font: 700 17px/1 "Arimo", sans-serif; letter-spacing: 1.5px; white-space: nowrap;
  }
  .spine-title { top: 26px; }
  .spine-author { top: 390px; font-size: 14px; letter-spacing: 0.5px; }

  /* Front cover */
  .front { left: 572px; width: 360px; }
  .front-photo {
    position: absolute; inset: 0;
    background:
      radial-gradient(ellipse 60% 45% at 50% 12%, #f4f7f6 0%, rgba(244,247,246,0) 70%),
      linear-gradient(180deg, #c9dbe6 0%, #9fbf8a 30%, #6f9a4c 48%, #a7ad9a 62%, #c7c7bd 80%, #b7b4a6 100%);
  }
  .shoe-photo {
    position: absolute; left: 30px; top: 290px; width: 210px; height: 150px;
    background:
      radial-gradient(ellipse 50% 34% at 52% 42%, rgba(110,30,55,0.85) 0%, rgba(110,30,55,0.55) 55%, rgba(110,30,55,0) 100%),
      radial-gradient(ellipse 48% 20% at 60% 78%, rgba(30,30,30,0.55) 0%, rgba(30,30,30,0) 100%);
  }
  .foreword { position: absolute; left: 0; right: 0; top: 26px; text-align: center; font: italic 400 15px/18px "Tinos", serif; color: var(--ink); }
  .title { position: absolute; inset: 0; font-family: "Archivo Black", sans-serif; font-weight: 400; line-height: 1; }
  .title span { position: absolute; white-space: nowrap; }
  .title .t1 { left: 52px; top: 70px; font-size: 50px; color: var(--title-green); transform: scaleY(1.3); transform-origin: left top; }
  .title .t2 { left: 80px; top: 134px; font-size: 58px; color: var(--title-light); transform: scaleY(1.15); transform-origin: left top; }
  .title .t3 { left: 82px; top: 202px; font-size: 62px; color: var(--paper); }
  .title .t4 {
    left: 118px; top: 384px; font-size: 38px; color: var(--step-ink);
    transform: rotate(6deg) skewX(-14deg); letter-spacing: 1px;
  }
  .front-author { position: absolute; left: 0; right: 0; top: 461px; text-align: center; font: 700 15px/1 "Arimo", sans-serif; color: var(--ink); }

  /* Message flap */
  .flap-message { left: 932px; width: 203px; background: var(--paper); border-left: 1px solid #d5d8d6; padding: 26px 22px 0 22px; color: var(--text-green); }
  .message { font: 400 13.5px/15.3px "Tinos", serif; text-align: justify; }
  .message .dropcap { font-size: 56px; line-height: 44px; }
  .message strong { font-weight: 700; }
  .quote { margin-top: 22px; font: italic 400 11.5px/14px "Tinos", serif; text-align: center; }
  .quote cite { display: block; margin-top: 6px; font-style: italic; text-align: right; }
</style>
</head>
<body>
<div class="canvas">
  <div class="jacket">

    <section class="panel flap-author">
      <span class="deco" style="left:90px;top:-30px;width:120px;height:120px;"></span>
      <span class="deco" style="left:70px;top:420px;width:140px;height:140px;"></span>
      <h2>About the Author</h2>
      <p class="bio"><span class="dropcap">C</span>olin Barr, lives in Singapore, certified coach NCAS (National Coaching and Accredited Scheme) level 3 in athletics and Basic Exercise Course (BEC). His races range from 1 to 50 km. He has competed more than 20 marathons locally and internationally. He has worked as a running coach, guest speaker.</p>
      <p class="bio"><span class="dropcap">V</span>olunteered as trainer for VANTRA and had spent the past 10 years exerting his influence from training programme to race execution for many. Contributed to Stride Weekly magazine in Running programme.</p>
    </section>

    <section class="panel back">
      <div class="back-photo" role="img" aria-label="Photo of an empty asphalt road fading into white, trees at the left edge"></div>
      <h3 class="back-head">Only by altering your mind,can you change your life</h3>
      <p class="back-sub">...and shape yourself</p>
      <div class="back-copy">
        <p>Remember, you are your own potter, mould your own clay. In other words, you have got to shape yourself, if not, someone else will!</p>
        <p>The Personal Best Timings clocked by the members of the 'REACH FURTHER' Team in many races completed – both local and overseas- speaks volume and testify to the essence of what this book is really about. It is simply not just about running…..it is about COURAGE.</p>
      </div>
      <p class="year">2012</p>
    </section>

    <section class="panel spine">
      <p class="spine-title">BEYOND THE FAR HILL</p>
      <p class="spine-author">Colin Barr</p>
    </section>

    <section class="panel front">
      <div class="front-photo" role="img" aria-label="Photo of a sunlit country road running between green trees toward distant hills"></div>
      <div class="shoe-photo" role="img" aria-label="Photo of a maroon Talvex running shoe landing forefoot-first on the road, casting a shadow"></div>
      <p class="foreword">Foreword by R. Delmonte<br>Lorem Ipsum is simply</p>
      <h1 class="title">
        <span class="t1">BEYOND</span>
        <span class="t2">THE</span>
        <span class="t3">far</span>
        <span class="t4">HILL</span>
      </h1>
      <p class="front-author">Colin Barr</p>
    </section>

    <section class="panel flap-message">
      <p class="message"><span class="dropcap">A</span>s a runner, we must learn to make up our mind and choose actions that reflect our relationship with the new positive self-image (YES, I CAN!) and not the old master – past conditioning (NO, I CAN'T!). The impetus to break free from the old master and transform oneself is to have <strong>FAITH</strong> in oneself and adopt the attitude of <strong>COURAGE</strong> to develop a purpose in running and set personal best timings to pursue. Learn to let go of your past and believe you can. After all, you will never know how high you can soar till you spread your wings.</p>
      <blockquote class="quote">"The greatest discovery of our age is that human can alter their lives by altering their attitude of mind."
        <cite>Howard Lindqvist, the noted Kingsbridge Psychologist</cite>
      </blockquote>
    </section>

  </div>
</div>
</body>
</html>
```